Business Cards for Orvanta LLC

We need business cards for a new company called “Orvanta LLC”. This is a technology process improvement company providing a comprehensive assessment of the technology used to run their business. The documentation and review process delivers the visibility and reassurance they need to protect their business and plan for the future. The product is called “Systems Mapwork”. Our primary target is small-medium size businesses, with the deliverables going to the decision maker. We would like to see the designs use the color blue. Our tag line is PROTECT YOUR BUSINESS · TAKE CONTROL OF IT.

Industry/Entity Type

Business

Contact Information for Business Card

Tag line should be on back of card - it does not have to be upper case.

Requirements
Must have
• Please use information when laying out card:
• Name: Gareth Pellham
• Title: Partner
• Phone Number: (844)555-0172
• Email: gareth@orvantallc-example.com
• Website: http://orvantallc-example.com

```html
<!DOCTYPE html>
<html lang="en">
<head>
<meta charset="utf-8">
<title>Business Cards for Orvanta LLC</title>
<link href="https://fonts.googleapis.com/css2?family=Montserrat:wght@400;500;700&display=swap" rel="stylesheet">
<style>
  :root {
    --brand-blue: #1a6fc2;
    --ink-gray: #6b6b6b;
    --rule-gray: #a9a9a9;
    --card-white: #ffffff;
    --stage: #eceeef;
  }
  * { margin: 0; padding: 0; box-sizing: border-box; }
  html, body { width: 960px; height: 1200px; overflow: hidden; }
  body {
    background: var(--stage);
    font-family: "Montserrat", sans-serif;
    position: relative;
  }
  .card {
    position: absolute;
    left: 130px;
    width: 700px;
    height: 400px;
    background: var(--card-white);
    box-shadow: 0 6px 24px rgba(0,0,0,0.12);
  }
  .card-front { top: 95px; }
  .card-back { top: 705px; }

  .front-name {
    position: absolute;
    inset: 0;
    display: flex;
    align-items: center;
    justify-content: center;
    gap: 16px;
    color: var(--brand-blue);
    font-weight: 700;
    font-size: 46px;
    letter-spacing: 2px;
  }
  .front-name .mark {
    width: 40px; height: 40px;
    background: var(--brand-blue);
  }

  .back-header {
    position: absolute;
    top: 40px; right: 44px;
    text-align: right;
  }
  .back-name {
    color: var(--brand-blue);
    font-weight: 700;
    font-size: 34px;
    letter-spacing: 1px;
    line-height: 1.1;
  }
  .tagline {
    margin-top: 12px;
    color: var(--ink-gray);
    font-size: 13px;
    font-weight: 500;
    letter-spacing: 0.5px;
  }
  .rule {
    position: absolute;
    height: 1px;
    background: var(--rule-gray);
  }
  .rule-top { top: 200px; left: 300px; right: 40px; }
  .rule-bottom { top: 330px; left: 40px; right: 300px; }

  .contact-row {
    position: absolute;
    display: flex;
    align-items: center;
    gap: 8px;
    color: var(--ink-gray);
    font-size: 15px;
    font-weight: 400;
  }
  .contact-row svg { width: 18px; height: 18px; flex: none; }
  .website { top: 216px; right: 44px; }
  .email { top: 346px; left: 44px; }

  .person {
    position: absolute;
    left: 44px;
    top: 240px;
  }
  .person-name {
    font-size: 26px;
    font-weight: 700;
    color: var(--ink-gray);
    letter-spacing: 0.5px;
  }
  .person-name .surname { color: var(--brand-blue); }
  .person-meta {
    margin-top: 4px;
    display: flex;
    align-items: center;
    gap: 14px;
    color: var(--ink-gray);
  }
  .person-title { font-size: 20px; font-weight: 400; }
  .divider { width: 1px; height: 20px; background: var(--ink-gray); }
  .person-phone { font-size: 14px; }
</style>
</head>
<body>
  <section class="card card-front" aria-label="Card front">
    <div class="front-name"><span class="mark"></span><span>Orvanta LLC</span></div>
  </section>

  <section class="card card-back" aria-label="Card back">
    <div class="back-header">
      <div class="back-name">Orvanta LLC</div>
      <div class="tagline">Protect your business · Take control of IT</div>
    </div>

    <div class="rule rule-top"></div>
    <div class="contact-row website">
      <svg viewBox="0 0 18 18" aria-hidden="true">
        <circle cx="9" cy="9" r="9" fill="var(--brand-blue)"/>
        <g fill="none" stroke="#fff" stroke-width="1">
          <circle cx="9" cy="9" r="5"/>
          <ellipse cx="9" cy="9" rx="2.2" ry="5"/>
          <line x1="4" y1="9" x2="14" y2="9"/>
        </g>
      </svg>
      <span>www.orvantallc-example.com</span>
    </div>

    <div class="person">
      <div class="person-name">GARETH <span class="surname">PELLHAM</span></div>
      <div class="person-meta">
        <span class="person-title">Partner</span>
        <span class="divider"></span>
        <span class="person-phone">(844)555-0172</span>
      </div>
    </div>

    <div class="rule rule-bottom"></div>
    <div class="contact-row email">
      <svg viewBox="0 0 18 18" aria-hidden="true">
        <circle cx="9" cy="9" r="9" fill="var(--brand-blue)"/>
        <rect x="4.5" y="6" width="9" height="6.5" fill="none" stroke="#fff" stroke-width="1"/>
        <polyline points="4.5,6 9,9.8 13.5,6" fill="none" stroke="#fff" stroke-width="1"/>
      </svg>
      <span>gareth@orvantallc-example.com</span>
    </div>
  </section>
</body>
</html>
```